E-commerce portal dedicated for selling books

We are looking for a design of a professional and official e-commerce web-site for a new company that is specialized in selling books (both books formats, printed and electronic), we’ll deal also with used-books where we plan to buy used books and re-sell them to other clients, or let the clients can sell their used-books directly to another client,
Web site must be very clear for users who like to brows the site contents or to buy a book, we will make the books available in discounted prices.
Customer should be able to perform the following actions in the site:
Search the book he/she is looking for easily
Get a brief description and details about the author, publisher, book content, browse the book’s content, browse first 20 pages ,
View similar or related books and a list of books that other users who bought this books also bought
Read and write reviews
Sign-up in the site
Complete the purchase process
Users can also sell or buy used-books from the site.
Look and feel:
The site’s look and feel is preferred to be clean, simple and balanced
Web site design is preferred to be simple with no strong or dark colors
User should feel comfort when looking at the home page because the design simplicity and comfortable colors
I liked the following sites’ look and feel:
http://www.lumirat.ae/
http://www.zelvik.com/
http://www.quillandfernbooks.com/
Please be sure to include all common elements that are used in the e-commerce web sites like Search, online form(s), shopping cart / ordering, user log in/member, printer-friendly function, subscription to newsletter.....
Industry/Entity Type
E-Commerce
Look and feel

```html
<!DOCTYPE html>
<html lang="en">
<head>
<meta charset="utf-8">
<title>Ecommerce Portal – Books</title>
<link rel="stylesheet" href="https://fonts.googleapis.com/css2?family=Arimo:wght@400;700&family=Oswald:wght@300;400;600&display=swap">
<style>
:root{
  --ink:#222;
  --muted:#666;
  --blue:#1f8fd0;
  --blue-dark:#1676b2;
  --line:#e2e2e2;
  --panel:#f1f1f1;
  --red:#d02a2a;
  --footer:#c9c9c9;
}
*{box-sizing:border-box;margin:0;padding:0}
html,body{width:834px;height:1200px;overflow:hidden;background:#fff}
body{font-family:Arimo,Arial,sans-serif;color:var(--ink)}
.page{width:1000px;height:1439px;transform:scale(.834);transform-origin:0 0;position:relative}
.abs{position:absolute}
.display{font-family:Oswald,"Arial Narrow",sans-serif}

.brand{left:125px;top:31px}
.brand-name{font-size:19px;font-weight:700;color:#333}
.brand-name span{color:var(--blue)}
.brand-slogan{font-size:11px;font-weight:700;color:#333;margin-top:-2px}

.searchbar{left:125px;top:86px;width:750px;height:37px;border:1px solid #d6d6d6;background:#f6f6f6;display:flex;align-items:center}
.search-icon{width:36px;height:31px;background:var(--blue);margin-left:4px;display:flex;align-items:center;justify-content:center;clip-path:polygon(0 0,85% 0,100% 50%,85% 100%,0 100%)}
.search-input{width:262px;height:27px;margin-left:2px;background:#fff;border:1px solid #ddd;font-size:11px;font-style:italic;color:#999;padding:7px 8px}
.search-cat{width:128px;height:27px;background:#fff;border:1px solid #ddd;font-size:10px;padding:8px 12px;display:flex;justify-content:space-between}
.search-btn{width:108px;height:29px;background:var(--blue);color:#fff;font-weight:700;font-size:14px;text-align:center;line-height:29px}
.account{font-size:10px;font-weight:700;padding-left:16px;line-height:13px;width:90px}
.account a,.nav-link a{color:var(--blue);text-decoration:none}
.nav-link{font-size:10px;font-weight:700;border-left:1px solid #ddd;padding:0 10px;line-height:13px}

.hero{left:125px;top:135px;width:750px;height:207px;background:var(--panel);border:1px solid #e4e4e4}
.hero-reader{left:18px;top:10px;width:118px;height:182px;background:#bbb;border:1px solid #aaa;border-radius:3px;padding:8px 8px 24px}
.hero-reader .cover{width:100%;height:100%;background:linear-gradient(160deg,#5b5a3c,#a8873f 60%,#3f3a2a)}
.hero-text{left:170px;top:28px;width:300px;text-align:center}
.hero-kicker{font-size:19px;letter-spacing:3px;font-weight:300}
.hero-rule{height:2px;background:linear-gradient(90deg,transparent,#ccc,transparent);margin:8px 0 20px}
.hero-the{left:175px;top:78px;font-size:15px}
.hero-title{left:175px;top:88px;font-size:46px;font-weight:400;letter-spacing:1px}
.hero-title i{font-size:40px}
.hero-sub{left:198px;top:158px;font-size:19px;letter-spacing:3px;font-weight:300;color:#555}
.hero-side{left:518px;top:0;width:230px;height:205px;background:#f7f7f7;border-left:1px solid #e4e4e4}
.hero-books{left:48px;top:18px;width:140px;height:130px}
.hero-cta{left:36px;top:166px;width:157px;height:30px;background:var(--blue);color:#fff;font-size:13px;text-align:center;line-height:30px;border-radius:3px}
.dots{left:812px;top:350px;display:flex;gap:4px}
.dots i{width:8px;height:8px;border-radius:50%;background:#888}
.dots i:first-child{background:var(--blue)}
.hero-shadow{left:125px;top:342px;width:750px;height:18px;background:linear-gradient(#eee,transparent)}

.section{left:125px;width:517px}
.section-head{display:flex;justify-content:space-between;align-items:flex-end;border-bottom:2px solid #eee;padding-bottom:6px}
.section-title{font-size:19px;font-weight:400;color:#222}
.see-all{font-size:11px;color:var(--blue)}
.row{position:relative;display:flex;gap:9px;margin-top:24px;padding-left:10px}
.arrow{position:absolute;top:58px;width:14px;height:22px;background:#fff;border:1px solid #ddd}
.arrow.left{left:-1px;border-radius:12px 0 0 12px}
.arrow.right{right:-16px;border-radius:0 12px 12px 0}
.arrow svg{display:block;margin:6px auto}
.book{width:95px;font-size:9px;line-height:15px}
.book .cover{width:95px;height:140px;border:1px solid #ccc;padding:3px;background:#fff;margin-bottom:12px}
.book .cover div{width:100%;height:100%}
.c1{background:#c8232a}
.c2{background:linear-gradient(#e8e4d6,#cfcabb)}
.c3{background:linear-gradient(#8c8c8c,#3b3b3b)}
.c4{background:#e8611b}
.c5{background:linear-gradient(135deg,#f5f5f5 50%,#151515 50%)}
.book-title{font-size:10px;color:var(--blue)}
.book-author{font-weight:700;padding-left:2px}
.stars{letter-spacing:1px;font-size:9px;padding-left:2px}
.price{padding-left:2px;margin-top:2px}

.ad{left:678px;top:397px;width:197px;height:164px;border:3px solid var(--red);text-align:center;background:#fff}
.ad-head{color:var(--red);font-weight:700;font-size:23px;line-height:29px;margin-top:10px}
.ad-name{margin:8px auto 0;width:165px;height:35px;background:#1d4aa8;color:#fff;font-weight:700;font-size:22px;line-height:35px;border-radius:4px}
.ad-line{color:#1d4aa8;font-weight:700;font-size:13px;margin-top:7px}
.ad-price{color:var(--red);font-size:13px}

.deal{left:678px;top:590px;width:197px;height:335px;background:#f7f7f7;border:1px solid #e6e6e6}
.deal-head{margin:0 10px;height:28px;background:#fff;text-align:center;font-size:15px;line-height:28px}
.deal-save{top:56px;width:100%;text-align:center;color:#d12;font-size:15px;font-style:italic}
.deal-book{left:50px;top:86px;width:87px;height:120px;border:4px solid #bbb;border-radius:3px;background:linear-gradient(#1e2f55,#3a1d5e 60%,#1e3d66)}
.deal-author{left:20px;top:242px;font-size:12px;color:var(--blue);font-style:italic;line-height:18px}
.deal-prices{right:24px;top:240px;text-align:right;font-size:11px;font-style:italic;line-height:23px}
.deal-prices b{color:#d12;font-weight:400}
.deal-btn{left:1px;bottom:0;width:194px;height:25px;background:var(--blue);color:#fff;font-size:12px;text-align:center;line-height:25px}

.news{left:678px;top:952px;width:197px;height:164px;background:#f2f0ea;border:1px solid #e0ddd4;text-align:center}
.news-title{font-size:15px;margin-top:10px}
.news-sub{font-size:11px;color:#555;margin-top:5px}
.news-input{margin:16px auto 0;width:173px;height:30px;background:#fff;border:1px solid #ccc;border-radius:4px;font-size:9px;color:#999;text-align:left;padding:9px 8px}
.news-btn{margin:17px 0 0 104px;width:79px;height:30px;background:var(--blue);color:#fff;font-size:13px;line-height:30px;border-radius:4px}

.footer{left:125px;top:1270px;width:750px;height:111px;border-top:1px solid #ddd;border-bottom:1px solid #ddd}
.fcol{position:absolute;top:10px;font-size:9px;color:#555;line-height:16px}
.fcol h4{font-size:11px;color:#222;margin-bottom:6px}
.fcol .cols{display:flex;gap:30px}
.social{display:flex;gap:8px;margin-top:2px}
.social i{width:25px;height:25px;border-radius:50%;background:#666}
.copyright{left:0;top:1390px;width:1000px;height:49px;background:var(--footer);color:#fff;font-size:9px;text-align:center;line-height:49px}
</style>
</head>
<body>
<div class="page">

  <div class="abs brand">
    <div class="brand-name">Ecommerce <span>Portal</span></div>
    <div class="brand-slogan">some slogan here</div>
  </div>

  <div class="abs searchbar">
    <div class="search-icon"><svg width="16" height="16" viewBox="0 0 16 16"><circle cx="9" cy="7" r="5" fill="none" stroke="#fff" stroke-width="2"/><line x1="5.5" y1="10.5" x2="1.5" y2="14.5" stroke="#fff" stroke-width="2.5"/></svg></div>
    <div class="search-input">Search</div>
    <div class="search-cat"><span>All Products</span><span>⌄</span></div>
    <div class="search-btn">Search</div>
    <div class="account">Hello. <a>Sign in</a><br><a>Your Account</a> ⌄</div>
    <div class="nav-link"><svg width="20" height="16" viewBox="0 0 20 16"><path d="M1 2h3l2 9h10l2-7H5" fill="none" stroke="#444" stroke-width="1.5"/><circle cx="8" cy="14" r="1.3" fill="#444"/><circle cx="15" cy="14" r="1.3" fill="#444"/></svg> <a>Cart</a> ⌄</div>
    <div class="nav-link">Wish<br><a>List</a> ⌄</div>
  </div>

  <div class="abs hero">
    <div class="abs hero-reader"><div class="cover" role="img" aria-label="Vintage poster book cover on an e-reader"></div></div>
    <div class="abs hero-text display"><div class="hero-kicker">THE LOREM IPSUM</div><div class="hero-rule"></div></div>
    <div class="abs hero-the display">THE</div>
    <div class="abs hero-title display">LOREM <i>of</i> IPSUM</div>
    <div class="abs hero-sub display">LOREM IPSUM DOLOR SIT</div>
    <div class="abs hero-side">
      <div class="abs hero-books" role="img" aria-label="Two stacked cream book covers" style="background:linear-gradient(160deg,transparent 10%,#e7e3d5 10%,#cfc9b6 80%,transparent 80%)"></div>
      <div class="abs hero-cta display">SHOP ALL MARTA ELLISON</div>
    </div>
  </div>
  <div class="abs hero-shadow"></div>
  <div class="abs dots"><i></i><i></i><i></i><i></i><i></i></div>

  <section class="abs section" style="top:385px">
    <div class="section-head"><h2 class="section-title display">Hot Books: Bestselling and in the News</h2><span class="see-all">See All ⌄</span></div>
    <div class="row">
      <span class="arrow left"><svg width="6" height="8"><path d="M5 0L0 4l5 4z" fill="#1f8fd0"/></svg></span>
      <div class="book"><div class="cover"><div class="c1" role="img" aria-label="Red book cover"></div></div><div class="book-title">Title of the Book...</div><div class="book-author">Author Name</div><div class="stars">★★★★★</div><div class="price">Price : $20.58</div></div>
      <div class="book"><div class="cover"><div class="c2" role="img" aria-label="Cream book cover"></div></div><div class="book-title">Title of the Book...</div><div class="book-author">Author Name</div><div class="stars">★★★★★</div><div class="price">Price : $20.58</div></div>
      <div class="book"><div class="cover"><div class="c3" role="img" aria-label="Grey photographic book cover"></div></div><div class="book-title">Title of the Book...</div><div class="book-author">Author Name</div><div class="stars">★★★★★</div><div class="price">Price : $20.58</div></div>
      <div class="book"><div class="cover"><div class="c4" role="img" aria-label="Orange book cover"></div></div><div class="book-title">Title of the Book...</div><div class="book-author">Author Name</div><div class="stars">★★★★★</div><div class="price">Price : $20.58</div></div>
      <div class="book"><div class="cover"><div class="c5" role="img" aria-label="Black and white book cover"></div></div><div class="book-title">Title of the Book...</div><div class="book-author">Author Name</div><div class="stars">★★★★★</div><div class="price">Price : $20.58</div></div>
      <span class="arrow right"><svg width="6" height="8"><path d="M0 0l5 4-5 4z" fill="#1f8fd0"/></svg></span>
    </div>
  </section>

  <section class="abs section" style="top:679px">
    <div class="section-head"><h2 class="section-title display">New Arrivals</h2><span class="see-all">See All ⌄</span></div>
    <div class="row">
      <span class="arrow left"><svg width="6" height="8"><path d="M5 0L0 4l5 4z" fill="#1f8fd0"/></svg></span>
      <div class="book"><div class="cover"><div class="c1" role="img" aria-label="Red book cover"></div></div><div class="book-title">Title of the Book...</div><div class="book-author">Author Name</div><div class="stars">★★★★★</div><div class="price">Price : $20.58</div></div>
      <div class="book"><div class="cover"><div class="c2" role="img" aria-label="Cream book cover"></div></div><div class="book-title">Title of the Book...</div><div class="book-author">Author Name</div><div class="stars">★★★★★</div><div class="price">Price : $20.58</div></div>
      <div class="book"><div class="cover"><div class="c3" role="img" aria-label="Grey photographic book cover"></div></div><div class="book-title">Title of the Book...</div><div class="book-author">Author Name</div><div class="stars">★★★★★</div><div class="price">Price : $20.58</div></div>
      <div class="book"><div class="cover"><div class="c4" role="img" aria-label="Orange book cover"></div></div><div class="book-title">Title of the Book...</div><div class="book-author">Author Name</div><div class="stars">★★★★★</div><div class="price">Price : $20.58</div></div>
      <div class="book"><div class="cover"><div class="c5" role="img" aria-label="Black and white book cover"></div></div><div class="book-title">Title of the Book...</div><div class="book-author">Author Name</div><div class="stars">★★★★★</div><div class="price">Price : $20.58</div></div>
      <span class="arrow right"><svg width="6" height="8"><path d="M0 0l5 4-5 4z" fill="#1f8fd0"/></svg></span>
    </div>
  </section>

  <section class="abs section" style="top:972px">
    <div class="section-head"><h2 class="section-title display">Related Books</h2><span class="see-all">See All ⌄</span></div>
    <div class="row">
      <span class="arrow left"><svg width="6" height="8"><path d="M5 0L0 4l5 4z" fill="#1f8fd0"/></svg></span>
      <div class="book"><div class="cover"><div class="c1" role="img" aria-label="Red book cover"></div></div><div class="book-title">Title of the Book...</div><div class="book-author">Author Name</div><div class="stars">★★★★★</div><div class="price">Price : $20.58</div></div>
      <div class="book"><div class="cover"><div class="c2" role="img" aria-label="Cream book cover"></div></div><div class="book-title">Title of the Book...</div><div class="book-author">Author Name</div><div class="stars">★★★★★</div><div class="price">Price : $20.58</div></div>
      <div class="book"><div class="cover"><div class="c3" role="img" aria-label="Grey photographic book cover"></div></div><div class="book-title">Title of the Book...</div><div class="book-author">Author Name</div><div class="stars">★★★★★</div><div class="price">Price : $20.58</div></div>
      <div class="book"><div class="cover"><div class="c4" role="img" aria-label="Orange book cover"></div></div><div class="book-title">Title of the Book...</div><div class="book-author">Author Name</div><div class="stars">★★★★★</div><div class="price">Price : $20.58</div></div>
      <div class="book"><div class="cover"><div class="c5" role="img" aria-label="Black and white book cover"></div></div><div class="book-title">Title of the Book...</div><div class="book-author">Author Name</div><div class="stars">★★★★★</div><div class="price">Price : $20.58</div></div>
      <span class="arrow right"><svg width="6" height="8"><path d="M0 0l5 4-5 4z" fill="#1f8fd0"/></svg></span>
    </div>
  </section>

  <aside class="abs ad">
    <div class="ad-head">Office suites<br>expensive?</div>
    <div class="ad-name">Postvane</div>
    <div class="ad-line">Business Email System</div>
    <div class="ad-price">Just $1 per user /mo</div>
  </aside>

  <aside class="abs deal">
    <div class="deal-head display">Deal <i>of the</i> Day</div>
    <div class="abs deal-save display">Save 65% TODAY</div>
    <div class="abs deal-book" role="img" aria-label="Dark blue and purple romance book cover"></div>
    <div class="abs deal-author display">Elena<br>Marsh</div>
    <div class="abs deal-prices display">orig$35.00<br>now<b>$12.25</b><br>You Save $22.75</div>
    <div class="abs deal-btn display">View All Deals ▸</div>
  </aside>

  <aside class="abs news">
    <div class="news-title display">Newsletter Subscription</div>
    <div class="news-sub">Sign up for savings, news, updates.</div>
    <div class="news-input">Enter Your Email Address</div>
    <div class="news-btn display">SUBMIT</div>
  </aside>

  <footer class="abs footer">
    <div class="fcol" style="left:0"><h4>Portal Services</h4><div class="cols"><div>About Portal<br>Investor Relations<br>Careers at Portal</div><div>Advertise<br>Bulk Order Discounts<br>Bookfairs</div></div></div>
    <div class="fcol" style="left:237px"><h4>Shipping &amp; Delivery</h4>About Free Shipping<br>About Shipping<br>Shipping Rates<br>Store Returns</div>
    <div class="fcol" style="left:387px"><h4>Quick Help</h4><div class="cols"><div>Customer Service<br>Order Status<br>Easy Returns<br>Product Recalls</div><div>Sitemap<br>Contact Us</div></div></div>
    <div class="fcol" style="left:601px"><h4>Follow us on</h4><div class="social" aria-label="Social links"><i></i><i></i><i></i></div></div>
  </footer>
  <div class="abs copyright">Copyright © 2013 Ecommerce Portal. All Rights Reserved</div>
</div>
</body>
</html>
```